Web Design Project

I need designs (PSD only - no programming) for several pages of a new website helping train operators to manage key information about their traindrivers.
The main feature of this website is the management of personnel records (create, edit, search, delete). Another key aspect is the management of user privileges. Since this is a new website we also need a user friendly frontpage, pricing information and how it works sections.
This can be broken down into 9 pages for which we need designs (PSDs).
1. Home
2. Driver record
3. How it works
4. Pricing
5. User administration
6. Help
7. Record list view
8. Login
9. Registration
Navigation (not logged in) are: Home | How it works | Pricing | Customers | About us | Contact
Navigation (logged in) are: Overview | Administration | Manage records | Billing | Help | Contact
Footer: Customer logos | Awards | Terms & Conditions | Privacy
To provide the best support for you to come up with a strong design proposal I will provide DAILY feedback to all participants. We have also created concept mockups (attached) and example pages (below) for each section to give you a clear sense of what we look for.
The core concepts for a successful bid are that the website is EASY to understand, INTUITIVE to navigate, and SIMPLE to use. Most of our users lack technical background and are looking for tool to simplify their work.
The strongest participants (winner and close contenders) will have the opportunity to additional commissioned work on additional sections not included in this brief.
Example Pages (by section)
1. http://www.brovendale.example/site-keepers/
1. http://www.qvt.example/
1. http://www.mondaph.example/
1. http://www.gorvanquest.example/
2. http://www.snapveld.example/profile_edit.gne
3. https://www.tarn.example/how-it-works/
3. http://www.bulkvue.example/learn
4. http://www.pactheron.example/crm/editions-pricing.jsp
4. http://www.brovendale.example/site-keepers/prices
6. https://support.talvora.example/en-gb/
6. http://help.dealmeadow.example/contact_us
8. https://www.careweave.example/uas/login
8. https://www.dealmeadow.example/login
8. http://www.askhollow.example/login/index
For form designs we like Verindo, Bidnook, Snapveld, CareWeave, Chatterly and the concepts presented by Tomas Kerrigan in his classic Layout Craft Shaping the Input Boxes.
For additional guidance see mockups attached!
Target Market(s)
Security, human resources and admin support employees for train operators.
Industry/Entity Type
Learn
Requirements
Should not have
- Home page should not have
Social media icons (chatterly, chirpla, CareWeave, RSS feed)
Contact forms
Read more links
Old trains

```html
<!DOCTYPE html>
<html lang="en">
<head>
<meta charset="utf-8">
<title>Train Driver Records – Home</title>
<link href="https://fonts.googleapis.com/css2?family=Cabin:wght@400;500;600&display=swap" rel="stylesheet">
<style>
  :root{
    --green:#2f6736;
    --page:#e8e8e8;
    --page-light:#efefef;
    --white:#ffffff;
    --ink:#333333;
    --ink-soft:#4a4a4a;
    --muted:#707070;
    --card:#d0caca;
    --black:#000000;
  }
  *{margin:0;padding:0;box-sizing:border-box}
  html,body{width:960px;height:1200px;overflow:hidden}
  body{position:relative;background:var(--page);font-family:"Cabin",Arial,sans-serif;color:var(--ink)}
  .header-band{position:absolute;left:0;top:0;width:960px;height:411px;background:var(--green)}
  .lower-band{position:absolute;left:0;top:1028px;width:960px;height:172px;background:var(--page-light)}

  .utility-nav{position:absolute;left:675px;top:0;width:239px;height:41px;background:var(--white);border-radius:0 0 0 12px;box-shadow:3px 3px 4px rgba(0,0,0,.45);display:flex;align-items:center;justify-content:center;gap:12px;font-size:14px;font-weight:500;color:var(--muted);z-index:3}

  .brand{position:absolute;left:35px;top:37px;width:221px;height:87px;background:var(--white);border:2px solid #dcdcdc;text-align:center;padding-top:10px;z-index:3}
  .brand-tail{position:absolute;left:35px;top:122px;width:30px;height:34px;background:var(--white);border:2px solid #dcdcdc;border-top:none;border-radius:0 0 0 10px;z-index:3}
  .brand-name{font-size:37px;font-weight:600;color:var(--green);line-height:1;letter-spacing:.5px}
  .brand-slogan{font-size:14px;font-weight:500;color:var(--muted);margin-top:6px;margin-left:-30px}

  .main-nav{position:absolute;left:370px;top:66px;display:flex;gap:11px;font-size:16.5px;font-weight:500;color:var(--white);z-index:3}

  .slider{position:absolute;left:35px;top:110px;width:879px;height:340px;background:var(--white);border:2px solid #3a3a3a}
  .slider-pointer{position:absolute;left:382px;top:94px;width:0;height:0;border-left:12px solid transparent;border-right:12px solid transparent;border-bottom:17px solid var(--white)}
  .slide-photo{position:absolute;left:13px;top:14px;width:847px;height:305px;background:linear-gradient(90deg,#3d4050 0%,#6c7a5a 22%,#93a07a 40%,#8a8a7e 55%,#7c8a63 72%,#3f6a2e 100%)}
  .slider-arrow{position:absolute;width:60px;height:60px;border-radius:50%;background:rgba(235,235,235,.85)}
  .slider-arrow svg{position:absolute;left:15px;top:15px}
  .slider-arrow.prev{left:21px;top:123px}
  .slider-arrow.next{left:788px;top:136px}
  .slide-tabs{position:absolute;left:665px;top:280px;display:flex;gap:2px}
  .slide-tab{width:39px;height:41px;background:var(--white);border:2px solid #e0e0e0;border-bottom:none;border-radius:8px 8px 0 0;font-size:20px;text-align:center;line-height:44px;color:var(--black)}

  .panel{position:absolute;left:32px;width:882px;background:var(--white)}
  .benefits{top:465px;height:253px}
  .how-it-works{top:738px;height:342px}
  .section-tag{position:absolute;left:3px;height:37px;background:var(--ink);color:var(--white);border-radius:0 12px 12px 0;font-size:21px;font-weight:500;line-height:37px;padding:0 14px 0 16px;letter-spacing:.3px;white-space:nowrap}
  .benefits .section-tag{top:10px;width:189px}
  .how-it-works .section-tag{top:20px;width:300px;padding-left:11px}
  .benefits-text{position:absolute;left:34px;top:57px;width:812px;font-size:13.6px;font-weight:500;line-height:33px;text-align:justify;color:var(--ink-soft)}

  .step{position:absolute;top:92px;width:279px;height:237px;background:var(--card);border:2px solid var(--ink)}
  .step--signup{left:12px}
  .step--login{left:303px}
  .step--update{left:592px}
  .step-title{text-align:center;font-size:25px;font-weight:500;color:var(--ink-soft);margin-top:14px;letter-spacing:.5px}
  .step-number{width:58px;height:58px;border-radius:50%;background:var(--white);margin:10px auto 0;box-shadow:3px 4px 4px rgba(0,0,0,.5);font-size:33px;text-align:center;line-height:58px;color:var(--black)}
  .step-text{position:absolute;left:17px;right:14px;font-size:14px;font-weight:500;color:var(--ink-soft)}
  .step--signup .step-text{top:146px;line-height:23px}
  .step--login .step-text{top:142px;line-height:33px}
  .step--update .step-text{top:149px;line-height:23px;left:23px}

  .callback-tab{position:absolute;left:869px;top:675px;width:91px;height:122px;background:var(--green);border-radius:10px 0 0 10px;box-shadow:2px 3px 4px rgba(0,0,0,.45);color:var(--white);font-size:14px;font-weight:500;line-height:23.5px;text-align:center;padding-top:10px;z-index:3}

  .site-footer{position:absolute;left:34px;top:1100px;width:880px;height:59px;background:var(--black);color:var(--white);display:flex;align-items:center;justify-content:center;gap:12px;font-size:16.5px;font-weight:500}
</style>
</head>
<body>
  <div class="header-band"></div>
  <div class="lower-band"></div>

  <nav class="utility-nav">
    <span>Sign Up</span><span>|</span><span>Login</span><span>|</span><span>Language</span>
  </nav>

  <nav class="main-nav">
    <span>Home</span><span>|</span>
    <span>How it works</span><span>|</span>
    <span>Prices</span><span>|</span>
    <span>Our Customer</span><span>|</span>
    <span>About us</span><span>|</span>
    <span>Contact</span>
  </nav>

  <section class="slider">
    <div class="slide-photo" role="img" aria-label="Photo of a train driver's cab view and a passenger train on curving tracks under a stone bridge"></div>
    <div class="slider-arrow prev">
      <svg width="30" height="30" viewBox="0 0 30 30"><path d="M20 3 L8 15 L20 27" fill="none" stroke="#000" stroke-width="6"/></svg>
    </div>
    <div class="slider-arrow next">
      <svg width="30" height="30" viewBox="0 0 30 30"><path d="M10 3 L22 15 L10 27" fill="none" stroke="#000" stroke-width="6"/></svg>
    </div>
    <div class="slide-tabs">
      <div class="slide-tab">1</div><div class="slide-tab">2</div><div class="slide-tab">3</div>
    </div>
  </section>
  <div class="slider-pointer"></div>

  <div class="brand-tail"></div>
  <div class="brand">
    <div class="brand-name">LOGO</div>
    <div class="brand-slogan">My Slogan</div>
  </div>

  <section class="panel benefits">
    <h2 class="section-tag">List&nbsp; of&nbsp; Benefits</h2>
    <p class="benefits-text">Lorem Ipsum is simply dummy text of the printing and typesetting industry. Lorem Ipsum has been the industry's standard dummy text ever since the 1500s, when an unknown printer took a galley of type and scrambled it to make a type specimen book. It has survived not only five centuries, but also the leap into electronic typesetting, remaining essentially unchanged. It was popularised in the 1960s with the release of Typeleaf sheets containing Lorem Ipsum passages, and more recently with desktop publishing software like Pressly Layoutmaker including versions of Lorem Ipsum.</p>
  </section>

  <section class="panel how-it-works">
    <h2 class="section-tag">Description Of&nbsp; how it works</h2>
    <div class="step step--signup">
      <h3 class="step-title">SIGN UP</h3>
      <div class="step-number">1</div>
      <p class="step-text">New user to register for their their first login.....</p>
    </div>
    <div class="step step--login">
      <h3 class="step-title">LOGIN</h3>
      <div class="step-number">2</div>
      <p class="step-text">Registered user login to update their profile and datas..</p>
    </div>
    <div class="step step--update">
      <h3 class="step-title">UPDATE</h3>
      <div class="step-number">3</div>
      <p class="step-text">Logged users can update current information and data..</p>
    </div>
  </section>

  <aside class="callback-tab">Request<br>a call<br>or<br>Sign up</aside>

  <footer class="site-footer">
    <span>Customer&nbsp; logos</span><span>|</span>
    <span>Awards</span><span>|</span>
    <span>Terms &amp; Condition</span><span>|</span>
    <span>Company Registration</span>
  </footer>
</body>
</html>
```